Church Music Album Cover

We are a Christian church in the OKC metro that is releasing a CD of songs that have connected with our congregation over the past few years. We are a church of about 1500 people of all ages- so while we want the design to be fresh, clean, and attractive- it doesn't have to be overly "youthy" or "edgy." Per the CD distribution company, the art image file you create should be able to be delivered with these requirements met:1400 x 1400 pixels minimum; 3000 x 3000 pixels maximumPNG, GIF, JPG, or JPEG file type72 - 300dpi (300dpi is the best)Less than 25mbRGB color scheme (not CMYK)
Updates

Thanks for submissions thus far. I realize my initial description may have not been the most helpful- and it some ways, I'm not 100% sure what I want. However, I would typically end to stay away from concrete images and tend to lean more towards earthy folk images. I don't even know if that makes sense. One google image search of the word "Grace" brings up individual letters spelling out Grace- each on a card clothes lined to a rope with out of focus lights or candles in the background. Another one had out of focus patio light bulbs lighting up the general text. Not sure why I like those and how they can connect to the theme, but I do. Another one had "Grace" on a pallet wall type background. Hopefully those are helpful suggestions.

Target Market(s)

Young parents- 30-40's

Colors

Requirements
Must have
• Title: Melodies from a Humble Porch
Nice to have
• Earthy/folky themes.
Should not have
• Bright colors

```html
<!DOCTYPE html>
<html lang="en">
<head>
<meta charset="utf-8">
<title>Melodies from a Humble Porch – Album Cover</title>
<link rel="stylesheet" href="https://fonts.googleapis.com/css2?family=Cinzel:wght@400&display=swap">
<style>
  :root {
    --night: #15131c;
    --dusk-violet: #2a2432;
    --sky-rose: #b9727f;
    --sky-peach: #e9c7bf;
    --water-slate: #3a3a4a;
    --lamp-amber: #f0a040;
    --title-white: #ffffff;
  }
  html, body {
    margin: 0;
    padding: 0;
    width: 1200px;
    height: 1200px;
    overflow: hidden;
    background: var(--night);
  }
  .album-cover {
    position: relative;
    width: 1200px;
    height: 1200px;
    overflow: hidden;
    background: var(--night);
  }
  .cover-photo {
    position: absolute;
    inset: 0;
    background:
      radial-gradient(ellipse 230px 190px at 660px 520px, rgba(240,160,64,0.75), rgba(240,160,64,0.25) 55%, transparent 80%),
      radial-gradient(ellipse 520px 110px at 820px 200px, rgba(233,199,191,0.55), transparent 75%),
      radial-gradient(ellipse 600px 120px at 880px 520px, rgba(185,114,127,0.45), transparent 75%),
      linear-gradient(90deg, rgba(16,14,22,0.95) 0%, rgba(16,14,22,0.6) 30%, transparent 55%),
      linear-gradient(180deg,
        var(--dusk-violet) 0%,
        #4a3a4c 12%,
        var(--sky-rose) 20%,
        #5a3e4c 26%,
        var(--night) 34%,
        #1c1820 40%,
        #8a5a66 47%,
        var(--water-slate) 58%,
        #23212d 72%,
        var(--night) 100%);
  }
  .cover-title {
    position: absolute;
    left: 0;
    top: 0;
    margin: 0;
    font-family: "Cinzel", "Trajan Pro", serif;
    font-weight: 400;
    font-size: 74px;
    line-height: 1;
    letter-spacing: 0.06em;
    color: var(--title-white);
  }
  .title-line {
    position: absolute;
    white-space: nowrap;
  }
  .title-line--first { left: 57px; top: 962px; }
  .title-line--second { left: 197px; top: 1052px; }
</style>
</head>
<body>
  <main class="album-cover">
    <div class="cover-photo" role="img" aria-label="Photograph of open hands holding glowing string lights against a blurred dusk sky reflected in a lake"></div>
    <h1 class="cover-title">
      <span class="title-line title-line--first">Melodies from a</span>
      <span class="title-line title-line--second">Humble Porch</span>
    </h1>
  </main>
</body>
</html>
```